Curl Dawn...restoring shine to thirsty, tired strands!

We are launching a luxurious, all-natural line of handmade hair products. These products will compete against a host of other not-so natural products targeting women with coily, kinky curly hair and the desire to grow (or re-grow) their tresses. Our product is different and we want our brand to reflect that. Curl Dawn is about bringing 'life back' to dry, damaged hair. Our product will be bottled in black or blue bottles and we'd love to see lime green accents in the concepts.

Target Market(s)

21 - 50 year old women with wavy, coily, curly or kinky hair.

Industry/Entity Type

Hair Care Product

Colors
add136
ffffff

Requirements
Must have
• Label must be "ready for retail" and catch a consumers eye when competing against other products. Should also look great online.
Nice to have
• Would love the label to include a symbol of "Life" or growth. The base of all the products is a plant called Moringa which is plant/superfood used in Africa and India. More information about Moringa can be found here
• http://www.glossmerit.com/articles/amazing-benefits-of-moringa-plant/
• Some of the benefits of Moringa include:
• Builds collagen fibers and minimize the appearance of fine wrinkle lines (Vitamin A)
• - Minimizes the appearance of fine wrinkle lines. (Vitamin C)
• - Improves moisturizing, softness and smoothness. (Vitamin E)
• - Delays the aging process
• - Helps build collagen which improves skin conditions
• - Is a natural healing emollient
• - Helps with dry, rough skin conditions like eczema, psoriasis and dermatitis.
• - Protects your skin from environmental damage
• - Helps improve scalp circulation (which aids in preventing hair loss)
• - Helps improve split ends in hair

```html
<!DOCTYPE html>
<html lang="en">
<head>
<meta charset="utf-8">
<title>Curl Dawn Hair Oil Label</title>
<link rel="stylesheet" href="https://fonts.googleapis.com/css2?family=Nunito:wght@700;800;900&family=Ubuntu:wght@400;500&display=swap">
<style>
  :root {
    --lime: #add136;
    --lime-soft: #d4eb8a;
    --leaf-dark: #4b6b0f;
    --leaf-mid: #5b7c14;
    --ink: #3f6410;
    --white: #ffffff;
  }
  html, body {
    margin: 0;
    padding: 0;
    overflow: hidden;
    background: var(--white);
  }
  .label {
    position: relative;
    width: 1200px;
    height: 933px;
    overflow: hidden;
    background: var(--white);
    font-family: "Ubuntu", sans-serif;
    color: var(--ink);
  }
  .abs { position: absolute; margin: 0; }

  .ring-cluster {
    position: absolute;
    border-radius: 50%;
    background: radial-gradient(circle, var(--lime) 0 30%, var(--lime-soft) 55%, rgba(173,209,54,0) 72%);
  }
  .ring-cluster--top { left: -20px; top: -25px; width: 195px; height: 160px; }
  .ring-cluster--bottom { left: 1020px; top: 700px; width: 150px; height: 110px; }

  .wave { position: absolute; left: 0; top: 0; }

  .brand-name {
    font-family: "Nunito", sans-serif;
    font-weight: 900;
    color: var(--leaf-dark);
    white-space: nowrap;
    line-height: 1;
  }
  .brand-sub {
    font-family: "Nunito", sans-serif;
    font-weight: 800;
    color: var(--leaf-dark);
    white-space: nowrap;
    line-height: 1;
  }
  .back .brand-name { left: 222px; top: 230px; font-size: 24px; }
  .back .brand-sub { left: 204px; top: 256px; font-size: 18px; }

  .heading {
    font-family: "Nunito", sans-serif;
    font-weight: 800;
    color: var(--leaf-mid);
    white-space: nowrap;
  }
  .usage-title { left: 131px; top: 312px; font-size: 17px; }
  .usage-text { left: 131px; top: 344px; font-size: 14.5px; line-height: 21.3px; }
  .ingredients-title { left: 129px; top: 431px; font-size: 17px; }
  .ingredients-text { left: 129px; top: 467px; font-size: 14.5px; line-height: 21.3px; }
  .origin { left: 129px; top: 606px; font-size: 17px; }
  .site { left: 129px; top: 634px; font-size: 17px; }

  .front .brand-name { left: 789px; top: 205px; font-size: 49px; }
  .front .brand-sub { left: 753px; top: 256px; font-size: 34px; }

  .tagline-band {
    left: 671px; top: 308px; width: 437px; height: 31px;
    background: var(--lime);
    border-bottom: 6px solid var(--leaf-mid);
    color: var(--white);
    font-family: "Nunito", sans-serif;
    font-weight: 800;
    font-size: 20.5px;
    text-align: center;
    line-height: 31px;
    white-space: nowrap;
  }
  .remedy-title { left: 755px; top: 388px; font-size: 18px; }
  .remedy-list {
    left: 757px; top: 431px;
    list-style: none; padding: 0;
    font-size: 14.5px;
  }
  .remedy-list li {
    position: relative;
    padding-left: 15px;
    height: 32px;
    line-height: 20px;
    white-space: nowrap;
  }
  .remedy-list li::before {
    content: "";
    position: absolute;
    left: 0; top: 8px;
    width: 6px; height: 6px;
    border-radius: 50%;
    background: var(--leaf-mid);
  }
  .volume {
    left: 798px; top: 660px; width: 200px;
    text-align: center;
    font-family: "Nunito", sans-serif;
    font-weight: 800;
    font-size: 18px;
    color: var(--leaf-dark);
  }
  .format-tag {
    left: 860px; top: 700px; width: 75px; height: 34px;
    background: var(--lime);
    color: var(--leaf-dark);
    font-family: "Nunito", sans-serif;
    font-weight: 900;
    font-size: 27px;
    text-align: center;
    line-height: 34px;
  }
  .purity-note {
    right: 101px; top: 854px;
    text-align: right;
    color: var(--white);
    font-size: 14px;
    line-height: 16.5px;
  }
</style>
</head>
<body>
<main class="label">
  <div class="ring-cluster ring-cluster--top" role="img" aria-label="Decorative cluster of lime green concentric rings"></div>

  <svg class="wave" width="1200" height="933" viewBox="0 0 1200 933" aria-hidden="true">
    <defs>
      <linearGradient id="waveFill" x1="0" y1="0" x2="0" y2="1">
        <stop offset="0" stop-color="#add136"/>
        <stop offset="0.7" stop-color="#b5d645"/>
        <stop offset="1" stop-color="#d2e98a"/>
      </linearGradient>
    </defs>
    <path d="M0 933 C 150 820, 330 765, 480 769 C 640 773, 790 830, 900 822 C 1010 814, 1130 760, 1200 676 L 1200 933 Z" fill="url(#waveFill)"/>
  </svg>

  <div class="ring-cluster ring-cluster--bottom" role="img" aria-label="Decorative cluster of white and lime concentric rings"></div>

  <section class="back">
    <p class="abs brand-name">Curl Dawn</p>
    <p class="abs brand-sub">Natural Pruduct</p>

    <h2 class="abs heading usage-title">How to Use:</h2>
    <p class="abs usage-text">Massage into scalp daily to stimulate growth.<br>Use as a hot oil treatment. Apply from root to tip<br>and to seal ends.</p>

    <h2 class="abs heading ingredients-title">The Remedy All Natural Ingredients:</h2>
    <p class="abs ingredients-text">Moringa Oil, African Castor Oil, Grapeseed Oil,<br>Avocado Oil, Sunflower Oil, Pumpkin Seed Oil,<br>Pumpkin Seed Extract, Green Tea Extract,<br>Nettle Extract, Essential of Rosemary, Lemon,<br>Green Tea, Patchouli, Cedarwood, Sage,<br>Chamomile and Lavender</p>

    <p class="abs heading origin">MADE IN THE USA</p>
    <p class="abs heading site">www.curldawnnaturals.com</p>
  </section>

  <section class="front">
    <h1 class="abs brand-name">Curl Dawn</h1>
    <p class="abs brand-sub">Natural Pruduct</p>

    <p class="abs tagline-band">Bring life back to dry, damaged tresses</p>

    <h2 class="abs heading remedy-title">The Remedy</h2>
    <ul class="abs remedy-list">
      <li>w/ Moringa and Castor Oil</li>
      <li>Daily, nourishing hair and scalp oil</li>
      <li>All Natural</li>
      <li>Hand-Made</li>
      <li>Paraben-free</li>
      <li>For daily sealing and care of all hair textures</li>
    </ul>

    <p class="abs volume">4 oz (118 ml)</p>
    <p class="abs format-tag">Oil</p>

    <p class="abs purity-note">No sulfites, mineral oils or synthetic<br>ingredients in this precious oil.</p>
  </section>
</main>
</body>
</html>
```